Book Cover Design - Uncovering Weight Loss Secrets

I need a book cover design for a book called 'Folding The Map'. It is a book that goes through all of the secrets to weight loss, without any crazy shakes or workouts or pills or potions. The book is really focused on helping people understand that Weight loss is simple and has more to do with our mindset as well as the food we were eating. It is about taking personal responsibility not looking for the next fancy revolutionary product that is going to help them magically melt the fat away. The book is pragmatic in nature and breaks down in simple terms how we can lose weight and keep it off for the rest of our lives. It shows the user that it is simple to lose weight, but it takes effort. They should stop looking for a quick fix when it comes to weight loss but instead eat healthy for the rest of their lives.
The book is intended to be hard-hitting no holds barred approach. The book has the same title as my business name. I will attach the current logo that we use in the business. This doesn't need to be on the front of the book maybe at the back down the bottom somewhere.
I am looking to have both an e-book cover and a standard printed book cover.
I don't have any colours in mind, my logo can be adapted to be different colours or just white.
The message that I am wanting people to feel when they see my book, is that all these Weightloss fads are a joke, that I know the secrets that will get them to their weight loss goal even if they fail at everything else before.
On the cover it should say the following.
FOLDING THE MAP
Uncovering the Weight Loss Secrets
The big companies have been trying to keep hidden for years!
COLIN MAYHEW
People who have failed many times trying to lose weight & need help
Weight Loss

```html
<!DOCTYPE html>
<html lang="en">
<head>
<meta charset="UTF-8">
<title>Folding The Map — Book Cover</title>
<link href="https://fonts.googleapis.com/css2?family=Montserrat:wght@600;700;800&family=Mrs+Saint+Delafield&display=swap" rel="stylesheet">
<style>
  :root {
    --page-bg: #f4f4f4;
    --cover-bg: #ffffff;
    --title-blue: #2b6cc4;
    --title-blue-light: #a9c3ea;
    --accent-red: #d63b3b;
    --ink: #1c1c1c;
    --photo-apple: #d8342a;
    --photo-tape: #4aa6e0;
    --photo-base: #f1f1f1;
  }
  * { margin: 0; padding: 0; box-sizing: border-box; }
  html, body {
    width: 1200px;
    height: 1200px;
    overflow: hidden;
    background: var(--page-bg);
  }
  .book-cover {
    position: absolute;
    left: 202px;
    top: 50px;
    width: 795px;
    height: 1100px;
    background: var(--cover-bg);
    font-family: "Montserrat", Arial, sans-serif;
    text-align: center;
  }
  .cover-title {
    position: absolute;
    left: 0;
    right: 0;
    top: 118px;
    font-weight: 800;
    font-size: 104px;
    line-height: 98px;
    letter-spacing: 1px;
    color: var(--title-blue);
  }
  .cover-title .title-line { display: block; }
  .cover-title .title-line--fade {
    background: linear-gradient(180deg, var(--title-blue) 25%, var(--title-blue-light) 100%);
    -webkit-background-clip: text;
    background-clip: text;
    color: transparent;
  }
  .cover-subtitle {
    position: absolute;
    left: 0;
    right: 0;
    top: 318px;
    font-weight: 700;
    font-size: 25px;
    letter-spacing: 8px;
    color: var(--accent-red);
  }
  .cover-photo {
    position: absolute;
    left: 91px;
    top: 360px;
    width: 675px;
    height: 500px;
    background:
      radial-gradient(ellipse 26% 34% at 52% 38%, var(--photo-apple) 0%, var(--photo-apple) 70%, rgba(216,52,42,0) 100%),
      radial-gradient(ellipse 50% 26% at 50% 68%, var(--photo-tape) 0%, rgba(74,166,224,0.7) 55%, rgba(74,166,224,0) 100%),
      radial-gradient(ellipse 60% 50% at 50% 55%, var(--photo-base) 0%, var(--cover-bg) 100%);
  }
  .cover-tagline {
    position: absolute;
    left: 0;
    right: 0;
    top: 912px;
    font-weight: 700;
    font-size: 15.5px;
    letter-spacing: 1.6px;
    color: var(--ink);
  }
  .cover-banner {
    position: absolute;
    left: 139px;
    top: 951px;
    width: 517px;
    height: 30px;
    background: var(--accent-red);
    color: #ffffff;
    font-weight: 700;
    font-size: 16.5px;
    letter-spacing: 1.8px;
    line-height: 30px;
  }
  .cover-author {
    position: absolute;
    left: 0;
    right: 0;
    top: 1008px;
    font-family: "Mrs Saint Delafield", cursive;
    font-size: 46px;
    color: var(--ink);
  }
</style>
</head>
<body>
  <main class="book-cover">
    <h1 class="cover-title">
      <span class="title-line">FOLDING</span>
      <span class="title-line title-line--fade">THE MAP</span>
    </h1>
    <p class="cover-subtitle">WEIGHT LOSS SECRETS</p>
    <div class="cover-photo" role="img" aria-label="Photo of a red apple wrapped in a blue measuring tape with a gold key resting beside it"></div>
    <p class="cover-tagline">FOR LOSING ALL THE WEIGHT YOU WANT &amp; KEEPING IT OFF FOREVER</p>
    <p class="cover-banner">NO MATTER WHAT YOU HAVE TRIED IN THE PAST</p>
    <p class="cover-author">Colin Mayhew</p>
  </main>
</body>
</html>
```